Business Card Design for Toriven

I've already got the logo, but I'd like to see some interesting designs.

I don't want anything to complex. I like it simple,yet innovative, like the logo.

My business is System Administration for small to medium size businesses, so that will be my main target audience.
Updates

hey all, the png has been uploaded.

Hey all,

If you are submitting the back side of the card, I'd like the top bit of the card to be Toriven Solutions and the logo, the bottom of the card the website, with a white background.

The middle I'd like to leave blank for a quote that will be printed on each card.

Thanks!

Dale

Industry/Entity Type

Business

```html
<!DOCTYPE html>
<html lang="en">
<head>
<meta charset="utf-8">
<title>Toriven Solutions – Business Cards</title>
<link rel="stylesheet" href="https://fonts.googleapis.com/css2?family=Lato:wght@400;700&display=swap">
<style>
  :root {
    --bg: #e9ecef;
    --card: #ffffff;
    --brand-blue: #2b7bbf;
    --ink: #2f2f2f;
    --ink-soft: #444444;
    --rule: #3a3a3a;
    --shadow: rgba(0, 0, 0, 0.18);
  }
  * { margin: 0; padding: 0; box-sizing: border-box; }
  html, body { width: 1200px; height: 960px; overflow: hidden; }
  body {
    background: var(--bg);
    font-family: "Lato", Arial, sans-serif;
    color: var(--ink);
    position: relative;
  }
  .card {
    position: absolute;
    left: 320px;
    width: 560px;
    height: 320px;
    background: var(--card);
    box-shadow: 0 6px 18px var(--shadow);
  }
  .card--front { top: 130px; }
  .card--back { top: 510px; }

  .brand {
    position: absolute;
    display: flex;
    align-items: center;
    gap: 12px;
  }
  .brand__dot {
    width: 46px; height: 46px;
    border-radius: 50%;
    background: var(--brand-blue);
  }
  .brand__name {
    font-size: 30px;
    font-weight: 700;
    color: var(--brand-blue);
    letter-spacing: 0.2px;
  }
  .card--front .brand { top: 36px; left: 34px; }
  .card--back .brand { top: 26px; left: 28px; }
  .card--back .brand__dot { width: 36px; height: 36px; }
  .card--back .brand__name { font-size: 24px; }

  .holder { position: absolute; left: 36px; top: 160px; }
  .holder__name { font-size: 30px; font-weight: 400; color: var(--ink); line-height: 1.1; }
  .holder__title { font-size: 17px; color: var(--ink-soft); margin-top: 6px; }

  .divider {
    position: absolute;
    left: 36px; right: 36px; top: 232px;
    border-top: 1.5px solid var(--rule);
  }

  .contacts {
    position: absolute;
    left: 36px; top: 246px;
    list-style: none;
    font-size: 16px;
    color: var(--ink);
  }
  .contacts li { display: flex; align-items: center; gap: 12px; height: 22px; }
  .contacts svg { width: 16px; height: 16px; fill: none; stroke: var(--brand-blue); stroke-width: 1.6; }

  .address {
    position: absolute;
    right: 36px; top: 246px;
    font-size: 14px;
    line-height: 22px;
    color: var(--ink);
  }
  .address__web { color: var(--brand-blue); font-weight: 700; }

  .footer-band {
    position: absolute;
    left: 0; right: 0; bottom: 38px;
    display: flex;
    align-items: center;
    gap: 8px;
  }
  .footer-band__lead { width: 18px; height: 5px; background: var(--brand-blue); }
  .footer-band__web { font-size: 15px; font-weight: 700; color: var(--brand-blue); letter-spacing: 0.3px; }
  .footer-band__bar { flex: 1; height: 7px; background: var(--brand-blue); }
</style>
</head>
<body>

<section class="card card--front" aria-label="Business card front">
  <div class="brand">
    <span class="brand__dot"></span>
    <span class="brand__name">Toriven Solutions</span>
  </div>

  <div class="holder">
    <p class="holder__name">Maren Holloway</p>
    <p class="holder__title">Operation Manager</p>
  </div>

  <div class="divider"></div>

  <ul class="contacts">
    <li>
      <svg viewBox="0 0 16 16" aria-hidden="true"><rect x="2" y="2" width="12" height="12" rx="1"/><rect x="4" y="4" width="3" height="8"/><line x1="9" y1="5" x2="12" y2="5"/><line x1="9" y1="8" x2="12" y2="8"/><line x1="9" y1="11" x2="12" y2="11"/></svg>
      (221) 33 604 18 27
    </li>
    <li>
      <svg viewBox="0 0 16 16" aria-hidden="true"><rect x="4" y="1.5" width="8" height="4"/><rect x="1.5" y="5.5" width="13" height="6" rx="1"/><rect x="4" y="9.5" width="8" height="5"/></svg>
      (221) 33 604 18 30
    </li>
    <li>
      <svg viewBox="0 0 16 16" aria-hidden="true"><rect x="1.5" y="3.5" width="13" height="9"/><polyline points="1.5,3.5 8,9 14.5,3.5"/></svg>
      name@toriven.com
    </li>
  </ul>

  <div class="address">
    <p>Rue des Palmiers - Mont Clair</p>
    <p>BP 218 - City, Country</p>
    <p class="address__web">www.toriven.com</p>
  </div>
</section>

<section class="card card--back" aria-label="Business card back">
  <div class="brand">
    <span class="brand__dot"></span>
    <span class="brand__name">Toriven Solutions</span>
  </div>

  <div class="footer-band">
    <span class="footer-band__lead"></span>
    <span class="footer-band__web">www.toriven.com</span>
    <span class="footer-band__bar"></span>
  </div>
</section>

</body>
</html>
```